Business Card- Can you make it cool vs boring!

Need a refresh on my business card! Want it to be modern but simple, classic and a pop of coolness! we do senior living and it is boring. but that doesn't mean our business card have to look boring! Open to two sided cards. our website is www.Bruvel-HQ.com

Target Market(s)

capital market

Industry/Entity Type

senior housing/ real estate

Contact Information for Business Card

logo/ name/ cell/ address/ www.Bruvel-HQ.com/ space for a QR code

Requirements
Must have
• maybe a QR code (do not make prominent I may not use the QR so design where it can be taken out) that link to more about us/ landing page. needs to be modern but clean
Should not have
• clip art or script

```html
<!DOCTYPE html>
<html lang="en">
<head>
<meta charset="utf-8">
<title>Bruvel Living – Business Card</title>
<link href="https://fonts.googleapis.com/css2?family=Lato:wght@300;400;700&display=swap" rel="stylesheet">
<style>
  :root {
    --page-bg: #e9e9e9;
    --card-bg: #ffffff;
    --brand: #a24a26;
    --ink: #3a3a3a;
    --muted: #8a8a8a;
    --rule: #c9c9c9;
  }
  * { box-sizing: border-box; margin: 0; padding: 0; }
  html, body { width: 1200px; height: 900px; overflow: hidden; }
  body {
    background: var(--page-bg);
    font-family: "Lato", sans-serif;
    color: var(--ink);
    position: relative;
  }
  .card {
    position: absolute;
    left: 250px;
    width: 700px;
    height: 400px;
    background: var(--card-bg);
    border-radius: 34px;
    box-shadow: 0 6px 20px rgba(0,0,0,0.12);
    overflow: hidden;
  }
  .card--front { top: 30px; }
  .card--back { top: 470px; }

  .wordmark {
    font-family: "Lato", sans-serif;
    font-weight: 400;
    color: var(--brand);
    white-space: nowrap;
  }

  /* Front */
  .front-brand {
    position: absolute;
    left: 0; right: 0;
    top: 130px;
    text-align: center;
    font-size: 58px;
    letter-spacing: 1px;
  }
  .front-rule {
    position: absolute;
    left: 190px; right: 130px;
    top: 232px;
    height: 1px;
    background: linear-gradient(90deg, rgba(201,201,201,0), var(--rule) 30%, var(--rule) 70%, rgba(201,201,201,0));
  }
  .front-url {
    position: absolute;
    left: 0; right: 0;
    top: 250px;
    text-align: center;
    font-size: 15px;
    font-weight: 700;
    letter-spacing: 7px;
    color: var(--muted);
  }
  .front-url .accent { color: var(--brand); }

  /* Back */
  .back-brand {
    position: absolute;
    left: 20px;
    width: 300px;
    top: 205px;
    text-align: center;
    font-size: 40px;
    letter-spacing: 0.5px;
  }
  .back-divider {
    position: absolute;
    left: 340px;
    top: 70px;
    width: 1px;
    height: 260px;
    background: linear-gradient(180deg, rgba(201,201,201,0), var(--muted) 50%, rgba(201,201,201,0));
  }
  .contact {
    position: absolute;
    left: 376px;
    top: 92px;
  }
  .contact-name {
    font-size: 20px;
    font-weight: 700;
    color: var(--brand);
    letter-spacing: 0.5px;
  }
  .contact-title {
    font-size: 17px;
    font-weight: 300;
    margin-top: 2px;
    padding-bottom: 6px;
    border-bottom: 1px solid var(--brand);
    width: 48px;
  }
  .contact-list { list-style: none; margin-top: 20px; }
  .contact-item {
    display: flex;
    align-items: flex-start;
    font-size: 16px;
    line-height: 1.35;
    margin-bottom: 7px;
  }
  .contact-icon {
    width: 16px; height: 16px;
    margin: 2px 10px 0 0;
    flex: none;
    fill: var(--brand);
  }
</style>
</head>
<body>

  <section class="card card--front" aria-label="Card front">
    <div class="front-brand wordmark">Bruvel Living</div>
    <div class="front-rule"></div>
    <div class="front-url">www.<span class="accent">Bruvel-HQ</span>.com</div>
  </section>

  <section class="card card--back" aria-label="Card back">
    <div class="back-brand wordmark">Bruvel Living</div>
    <div class="back-divider"></div>

    <div class="contact">
      <div class="contact-name">DANA MORROW</div>
      <div class="contact-title">CEO</div>
      <ul class="contact-list">
        <li class="contact-item">
          <svg class="contact-icon" viewBox="0 0 24 24"><path d="M6.6 10.8a15.1 15.1 0 0 0 6.6 6.6l2.2-2.2c.3-.3.7-.4 1-.2 1.1.4 2.3.6 3.6.6.6 0 1 .4 1 1V20c0 .6-.4 1-1 1A17 17 0 0 1 3 4c0-.6.4-1 1-1h3.5c.6 0 1 .4 1 1 0 1.3.2 2.5.6 3.6.1.3 0 .7-.2 1z"/></svg>
          555.014.2208
        </li>
        <li class="contact-item">
          <svg class="contact-icon" viewBox="0 0 24 24"><path d="M3 5h18a1 1 0 0 1 1 1v12a1 1 0 0 1-1 1H3a1 1 0 0 1-1-1V6a1 1 0 0 1 1-1zm0 2.2V17h18V7.2l-9 6-9-6zM4.5 7 12 12l7.5-5z"/></svg>
          hello@bruvel-hq.com
        </li>
        <li class="contact-item">
          <svg class="contact-icon" viewBox="0 0 24 24"><path d="M12 2a10 10 0 1 0 0 20 10 10 0 0 0 0-20zm6.9 9h-3a15 15 0 0 0-1.3-6A8 8 0 0 1 18.9 11zM12 4.1c.9 1.2 1.7 3.7 1.9 6.9h-3.8c.2-3.2 1-5.7 1.9-6.9zM9.4 5a15 15 0 0 0-1.3 6h-3A8 8 0 0 1 9.4 5zm-4.3 8h3a15 15 0 0 0 1.3 6A8 8 0 0 1 5.1 13zm6.9 6.9c-.9-1.2-1.7-3.7-1.9-6.9h3.8c-.2 3.2-1 5.7-1.9 6.9zm2.6-.9a15 15 0 0 0 1.3-6h3a8 8 0 0 1-4.3 6z"/></svg>
          www.Bruvel-HQ.com
        </li>
        <li class="contact-item">
          <svg class="contact-icon" viewBox="0 0 24 24"><path d="M12 2a7 7 0 0 0-7 7c0 5.2 7 13 7 13s7-7.8 7-13a7 7 0 0 0-7-7zm0 9.5A2.5 2.5 0 1 1 12 6.5a2.5 2.5 0 0 1 0 5z"/></svg>
          <span>4120 Meadowbrook Ln<br>Fairview, Tx 75069</span>
        </li>
      </ul>
    </div>
  </section>

</body>
</html>
```